Stylish new business card needed!

Hello everyone! I am in need of a new business card design for an alarm company here in Hurricane WV. I have all fonts, color codes and logos provided for you use! We are a young company and like the style of a clean sleek looking business card. Would like it double sided, one side holding the logo and the other with your design!
Target Market(s)
The people that are looking for the newest tech for home automation and security
Industry/Entity Type
Alarm services; Home automation
Contact Information for Business Card
Name of person; position (Sales; Installer); Phone Number (555.419.7362); Employee cell Number; Website (www.GuardedByVelm.example); Employee Email; Double sided
Look and feel
Each slider illustrates characteristics of the customer's brand and the style your logo design should communicate.

```html
<!DOCTYPE html>
<html lang="en">
<head>
<meta charset="utf-8">
<title>Guarded By Velm — Business Card</title>
<link rel="stylesheet" href="https://fonts.googleapis.com/css2?family=Arimo:wght@400;700&family=Montserrat:wght@500;800&display=swap">
<style>
  :root {
    --paper: #e9e9e9;
    --card: #2b2b2b;
    --card-deep: #141414;
    --recess: #262626;
    --disc: #3a3a3a;
    --disc-ring: #2f2f2f;
    --orange: #f07f2e;
    --edge: #d9692a;
    --white: #f4f4f4;
    --grey: #cfcfcf;
  }
  * { margin: 0; padding: 0; box-sizing: border-box; }
  html, body { width: 1200px; height: 802px; overflow: hidden; }
  body {
    background: var(--paper);
    font-family: "Arimo", Arial, sans-serif;
    position: relative;
  }
  .card {
    position: absolute;
    top: 246px;
    width: 540px;
    height: 310px;
    background: var(--card);
    border-bottom: 3px solid var(--edge);
    border-left: 2px solid var(--edge);
    overflow: hidden;
    box-shadow: 0 10px 24px rgba(0,0,0,.18);
  }
  .card--front { left: 40px; }
  .card--back { left: 620px; }

  /* Front */
  .brand-block {
    position: absolute;
    right: 40px;
    top: 36px;
  }
  .brand-name {
    font-family: "Montserrat", sans-serif;
    font-weight: 800;
    font-size: 30px;
    letter-spacing: 1px;
    color: var(--white);
    line-height: 1;
    white-space: nowrap;
  }
  .brand-tagline {
    margin-top: 10px;
    font-weight: 700;
    font-size: 8px;
    letter-spacing: .6px;
    color: var(--orange);
    white-space: nowrap;
  }
  .rule-brand {
    position: absolute;
    left: 172px; right: 28px; top: 100px;
    height: 1px; background: var(--orange);
  }
  .person {
    position: absolute;
    left: 60px; top: 150px;
  }
  .person-name {
    font-weight: 700;
    font-size: 18px;
    color: var(--orange);
    letter-spacing: .3px;
  }
  .person-role {
    margin-top: 2px;
    font-size: 14px;
    color: var(--white);
  }
  .rule-person {
    position: absolute;
    left: 60px; right: 220px; top: 198px;
    height: 1px; background: var(--orange);
  }
  .edge-tab {
    position: absolute;
    left: 0; top: 214px;
    width: 18px; height: 22px;
    background: var(--orange);
  }
  .contact {
    position: absolute;
    left: 90px; bottom: 30px;
    list-style: none;
    font-size: 14px;
    color: var(--grey);
  }
  .contact li { display: flex; align-items: center; gap: 10px; margin-top: 5px; white-space: nowrap; }
  .contact svg { width: 12px; height: 12px; }
  .website {
    position: absolute;
    right: 28px; bottom: 52px;
    font-size: 13px;
    color: var(--grey);
    white-space: nowrap;
  }
  .website .accent { color: var(--orange); }

  /* Back */
  .recess {
    position: absolute;
    left: 0; top: 0;
    width: 540px; height: 310px;
  }
  .back-disc {
    position: absolute;
    right: 18px; top: 28px;
    width: 254px; height: 254px;
    border-radius: 50%;
    background: var(--disc);
    display: flex; align-items: center; justify-content: center;
    box-shadow: inset 0 0 0 30px var(--disc-ring), 0 0 0 2px #1e1e1e;
  }
  .back-name {
    font-family: "Montserrat", sans-serif;
    font-weight: 800;
    font-size: 42px;
    letter-spacing: 1px;
    color: var(--white);
  }
</style>
</head>
<body>
  <section class="card card--front" aria-label="Business card front">
    <div class="brand-block">
      <div class="brand-name">GUARDED BY VELM</div>
      <div class="brand-tagline">AUTOMATION AND SECURITY SERVICES</div>
    </div>
    <div class="rule-brand"></div>

    <div class="person">
      <div class="person-name">MARCUS HALE</div>
      <div class="person-role">Sales / Installer</div>
    </div>
    <div class="rule-person"></div>
    <div class="edge-tab"></div>

    <ul class="contact">
      <li>
        <svg viewBox="0 0 12 12" aria-hidden="true"><path d="M2.5 1l2 2.2-1 1.2a6 6 0 0 0 4.1 4.1l1.2-1 2.2 2-1 1.5C5.5 11 1 6.5 1 2z" fill="none" stroke="#f07f2e" stroke-width="1.2"/></svg>
        555.419.7362
      </li>
      <li>
        <svg viewBox="0 0 12 12" aria-hidden="true"><rect x="1" y="2.5" width="10" height="7" fill="none" stroke="#f07f2e" stroke-width="1.2"/><path d="M1 3l5 3.5L11 3" fill="none" stroke="#f07f2e" stroke-width="1.2"/></svg>
        info@GuardedByVelm.example
      </li>
    </ul>
    <div class="website">www.<span class="accent">GuardedByVelm</span>.example</div>
  </section>

  <section class="card card--back" aria-label="Business card back">
    <svg class="recess" viewBox="0 0 540 310" aria-hidden="true">
      <circle cx="120" cy="230" r="140" fill="#141414"/>
      <circle cx="130" cy="222" r="106" fill="#262626"/>
    </svg>
    <div class="back-disc">
      <span class="back-name">VELM</span>
    </div>
  </section>
</body>
</html>
```